Drug Company Needs a Counter Display

********I am after a point of sale counter top display design. **********
^^^^^^^^^^^^^^^^^^^^^^^^^^^^^^^^^^^^^^^^^^^^^^^^^^

The design should somewhat match the current format of my products, be eye caching and modern. PLEASE REFERR TO THE ATTACHMENTS FOR INSPIRATION

What I had in mind for this project was;
If you can notice the counter display as shown in the picture with the products inside.
The bottom half of the product boxes have been cut off because of the front lip of the display, I was perhaps thinking that the display could have the bottom half of the box printed on it so it would give the illusion of a complete box.. This could be the same on the sides also, as it tapers up giving the illusion of a complete box.

I imagine possibly having the centre divider either black on the centre and then because the display is slightly larger than the boxes the "illusion" box on the left and right can be centered and then outlined with black lines.

The header board should have a clear catch phrase like "Drug Testing Kits"- easy to use -99% accuracy - fast results the text can be set on a contrasting background, solid colors are ok with gradients, swirls etc any graphic you think looks good.

Detection Times
*Depending on quantity
Ecstasy - 1 - 3 Days
Meth Amphetamine - 1 - 3 Days
Marijuana - 1 - 30 Days

This project is very open to creativity and designers can head in their own direction with this, I am not overly creative and my idea was only a suggestion.. I am keen to take on any eye catching yet professional design.

Thanks in advance.

Target Market(s)

Adults ages 18 - 45 in western speaking countries.

Industry/Entity Type

Drug

Requirements
Must have
• Easy to read text
Should not have
• cluttered text

```html
<!DOCTYPE html>
<html lang="en">
<head>
<meta charset="utf-8">
<title>Drug Testing Kit – Header Board</title>
<link rel="stylesheet" href="https://fonts.googleapis.com/css2?family=Arimo:wght@700&family=Noto+Serif:wght@700&display=swap">
<style>
  :root {
    --page: #ffffff;
    --board-edge: #0a0a0a;
    --board-glow: #7a0000;
    --title: #ffffff;
    --title-shadow: #1a1a1a;
    --tagline: #e8f21a;
    --label: #ffffff;
    --pill: #0b0b0b;
    --divider: #8a7a1c;
  }
  html, body {
    margin: 0;
    padding: 0;
    width: 1200px;
    height: 1000px;
    overflow: hidden;
    background: var(--page);
  }
  .canvas {
    position: relative;
    width: 1200px;
    height: 1000px;
  }
  .header-board {
    position: absolute;
    left: 27px;
    top: 342px;
    width: 1145px;
    height: 315px;
    background:
      radial-gradient(ellipse 52% 68% at 50% 48%, var(--board-glow) 0%, var(--board-glow) 55%, #3a0000 80%, var(--board-edge) 100%);
    background-color: var(--board-edge);
    text-align: center;
    font-family: "Arimo", Arial, sans-serif;
    font-weight: 700;
  }
  .title {
    margin: 0;
    position: absolute;
    left: 0; right: 0;
    top: 12px;
    font-family: "Noto Serif", Georgia, serif;
    font-size: 80px;
    line-height: 1;
    letter-spacing: 1px;
    color: var(--title);
    text-shadow: 2px 2px 0 #bbb, 4px 5px 0 var(--title-shadow), 5px 7px 3px #000;
  }
  .tagline {
    position: absolute;
    left: 0; right: 0;
    top: 112px;
    margin: 0;
    font-size: 39px;
    line-height: 1;
    color: var(--tagline);
    text-shadow: 2px 2px 2px #000;
  }
  .detection-label {
    position: absolute;
    left: 50%;
    top: 176px;
    transform: translateX(-50%);
    padding: 4px 20px 6px;
    border-radius: 24px;
    background: var(--pill);
    font-size: 35px;
    line-height: 1;
    color: var(--label);
    white-space: nowrap;
    text-shadow: 2px 2px 2px #555;
  }
  .detection-list {
    position: absolute;
    left: 0; right: 0;
    top: 234px;
    margin: 0;
    padding: 0;
    list-style: none;
    display: flex;
    justify-content: center;
    align-items: center;
    font-size: 27px;
    color: var(--label);
    text-shadow: 2px 2px 2px #000;
    white-space: nowrap;
  }
  .detection-list li {
    padding: 0 12px;
    line-height: 42px;
  }
  .detection-list li + li {
    border-left: 4px solid var(--divider);
  }
  .footnote {
    position: absolute;
    left: 0; right: 0;
    top: 287px;
    margin: 0;
    font-size: 18px;
    color: var(--label);
  }
</style>
</head>
<body>
<div class="canvas">
  <section class="header-board">
    <h1 class="title">Drug Testing Kit</h1>
    <p class="tagline">easy to use - 99% accuracy - fast results</p>
    <div class="detection-label">Detection Times</div>
    <ul class="detection-list">
      <li>Ecstasy - 1 - 3 Days</li>
      <li>Meth Amphetamine - 1 - 3 Days</li>
      <li>Marijuana - 1 - 30 Days</li>
    </ul>
    <p class="footnote">*Depending on quantity</p>
  </section>
</div>
</body>
</html>
```